Business Card for IT Support Company
Aide Nova
Business Card for IT Support Company - Information Technology
Creative Brief
Professional
Assistance Informatique 24/7
Tél. 0900 417 536
2.50 CHF/min de 8h à 22h et 3.50 CHF/min de 22h à 8h depuis le réseau fixe.
info@aide-nova.ch
http://www.aide-nova.ch
No specific name, this is only a hotline IT support number Business Card (phone number is in the title) in Address box, it's the rates on the Business Number. We will use brivopress . ch as the printing company, here are the exact size in mm they send to me: Business card Size is 85x55mm (But file dimension must be 91x61mm) Colors needs to be send in CMYK, minimum 200 dpi, maximum quality.
- Contrôle à distance PC/MAC - Support technique informatique - Formation / Consulting / Coaching - Infographie / Graphisme - Création de Site Web - Smartphone / Tablette

```html
<!DOCTYPE html>
<html lang="fr">
<head>
<meta charset="utf-8">
<title>Aide Nova – Carte de visite</title>
<link href="https://fonts.googleapis.com/css2?family=Exo+2:wght@600;700;800&display=swap" rel="stylesheet">
<style>
  :root {
    --page-bg: #e6e6e6;
    --card-white: #ffffff;
    --card-black: #0d0d0d;
    --brand-red: #e0202a;
    --brand-red-dark: #a8121a;
    --line-grey: #c9c9c9;
    --text-white: #ffffff;
    --text-grey: #6b6b6b;
  }
  html, body {
    margin: 0;
    padding: 0;
    width: 1200px;
    height: 901px;
    overflow: hidden;
    background: var(--page-bg);
    font-family: "Exo 2", Arial, sans-serif;
  }
  .business-card {
    position: absolute;
    left: 100px;
    top: 127px;
    width: 1000px;
    height: 647px;
    border-radius: 44px;
    background: var(--card-white);
    overflow: hidden;
    box-shadow: 0 10px 30px rgba(0,0,0,0.18);
  }
  .card-shapes {
    position: absolute;
    inset: 0;
    width: 1000px;
    height: 647px;
  }
  .brand-lockup {
    position: absolute;
    left: 72px;
    top: 120px;
    display: flex;
    align-items: center;
    gap: 34px;
  }
  .brand-dot {
    width: 120px;
    height: 120px;
    border-radius: 50%;
    background: var(--brand-red);
  }
  .brand-name {
    color: var(--text-white);
    font-weight: 700;
    font-size: 48px;
    letter-spacing: 1px;
    margin-top: -40px;
  }
  .web-contacts {
    position: absolute;
    left: 508px;
    top: 236px;
    color: var(--text-white);
    font-weight: 700;
    font-size: 25px;
    line-height: 34px;
    letter-spacing: 2px;
    text-transform: uppercase;
  }
  .call-block {
    position: absolute;
    left: 72px;
    top: 500px;
  }
  .call-label {
    color: var(--brand-red);
    font-weight: 800;
    font-size: 26px;
    letter-spacing: 2px;
    text-transform: uppercase;
  }
  .call-number {
    color: var(--text-grey);
    font-weight: 800;
    font-size: 50px;
    letter-spacing: 3px;
    line-height: 56px;
  }
</style>
</head>
<body>
  <div class="business-card">
    <svg class="card-shapes" viewBox="0 0 1000 647" aria-hidden="true">
      <path class="grey-rule" d="M0,505 C220,420 480,400 700,380 C820,368 920,352 1000,330" fill="none" stroke="var(--line-grey)" stroke-width="3"/>
      <path class="red-swoosh" d="M0,462 C200,390 450,372 680,352 C820,340 920,320 1000,300 L1000,322 C920,345 820,362 690,374 C460,392 220,412 0,492 Z" fill="var(--brand-red)"/>
      <path class="red-swoosh-shade" d="M0,478 C220,404 460,384 690,364 C820,352 920,334 1000,312 L1000,322 C920,345 820,362 690,374 C460,392 220,412 0,492 Z" fill="var(--brand-red-dark)"/>
      <path class="black-field" d="M0,0 H1000 V292 C920,315 820,334 680,346 C450,366 200,384 0,456 Z" fill="var(--card-black)"/>
    </svg>

    <div class="brand-lockup">
      <div class="brand-dot"></div>
      <div class="brand-name">Aide Nova 24/7</div>
    </div>

    <div class="web-contacts">
      <div class="contact-email">info@aide-nova.ch</div>
      <div class="contact-site">www.aide-nova.ch</div>
    </div>

    <div class="call-block">
      <div class="call-label">Call us today</div>
      <div class="call-number">0900 417 536</div>
    </div>
  </div>
</body>
</html>
```